Shampoo and Shower Gel Packaging Design

I need a new packaging design for a men shampoo and shower gel bottle. The packaging must me black (black bottle/package) and the logo should be also monochrom.
For example, black matte bottle and black shiny logo on the packaging (not mandatory).
the design must contain maximum 3 colors.
1. black
2. white (text)
3. grey/dark blue/dark green (colors will be the difference between products parfumes/smell/scences.

Design must be minimalist/elegant/discrete.
Updates

Please check the photos i added for pure inspiration.

Target Market(s)

brand exclusively for MEN - premium clients

Industry/Entity Type

Cosmetics

Font styles to use
Sans Serif

Colors
1b1b1b
5c5c5c
aaaaaa
ffffff
3176b5

Requirements
Must have
• black background
• minimalist design

```html
<!DOCTYPE html>
<html lang="en">
<head>
<meta charset="utf-8">
<title>Kaelo – Shampoo and Shower Gel Labels</title>
<link rel="stylesheet" href="https://fonts.googleapis.com/css2?family=Nunito+Sans:wght@300;400;600&display=swap">
<style>
  :root {
    --canvas-bg: #ffffff;
    --label-black: #121516;
    --ring-grey: #a9b1b1;
    --text-white: #ffffff;
    --volume-grey: #b4b8b8;
    --scent-teal: #3fb4b8;
    --scent-olive: #a9b82c;
  }
  html, body {
    margin: 0;
    padding: 0;
    width: 1200px;
    height: 655px;
    overflow: hidden;
    background: var(--canvas-bg);
  }
  .canvas {
    position: relative;
    width: 1200px;
    height: 655px;
  }
  .label {
    position: absolute;
    top: 62px;
    width: 525px;
    height: 525px;
    background: var(--label-black);
  }
  .label--shampoo { left: 50px; }
  .label--shower-gel { left: 627px; }
  .label svg {
    display: block;
    width: 525px;
    height: 525px;
    font-family: "Nunito Sans", sans-serif;
  }
  .ring { fill: none; stroke: var(--ring-grey); }
  .ring--outer { stroke-width: 4; }
  .ring--inner { stroke-width: 2.5; }
  .product-name {
    fill: var(--text-white);
    font-size: 21px;
    font-weight: 400;
    letter-spacing: 7px;
  }
  .scent {
    font-size: 23px;
    font-weight: 400;
    letter-spacing: 8px;
  }
  .scent--lavender { fill: var(--scent-teal); }
  .scent--bergamot { fill: var(--scent-olive); }
  .brand-dot { fill: var(--text-white); }
  .brand-name {
    fill: var(--text-white);
    font-size: 32px;
    font-weight: 300;
    letter-spacing: 9px;
  }
  .volume {
    fill: var(--volume-grey);
    font-size: 15px;
    font-weight: 400;
    letter-spacing: 3px;
  }
</style>
</head>
<body>
<main class="canvas">

  <section class="label label--shampoo" aria-label="Kaelo shampoo label, lavender mint">
    <svg viewBox="0 0 525 525" xmlns="http://www.w3.org/2000/svg">
      <defs>
        <path id="shampoo-top-arc" d="M 173.7,249.2 A 94 94 0 1 1 350.3,249.2"/>
        <path id="shampoo-bottom-arc" d="M 160.5,180.1 A 108 108 0 1 0 363.5,180.1"/>
      </defs>
      <circle class="ring ring--outer" cx="262" cy="217" r="120"/>
      <circle class="ring ring--inner" cx="262" cy="217" r="83"/>
      <text class="product-name" text-anchor="middle">
        <textPath href="#shampoo-top-arc" startOffset="50%">SHAMPOO</textPath>
      </text>
      <text class="scent scent--lavender" text-anchor="middle">
        <textPath href="#shampoo-bottom-arc" startOffset="50%">lavender mint</textPath>
      </text>
      <circle class="brand-dot" cx="262" cy="190" r="7"/>
      <text class="brand-name" x="266" y="245" text-anchor="middle">KAELO</text>
      <text class="volume" x="264" y="420" text-anchor="middle">4 FL. OZ.</text>
    </svg>
  </section>

  <section class="label label--shower-gel" aria-label="Kaelo shower gel label, bergamot">
    <svg viewBox="0 0 525 525" xmlns="http://www.w3.org/2000/svg">
      <defs>
        <path id="gel-top-arc" d="M 173.7,251.2 A 94 94 0 1 1 350.3,251.2"/>
        <path id="gel-bottom-arc" d="M 160.5,182.1 A 108 108 0 1 0 363.5,182.1"/>
      </defs>
      <circle class="ring ring--outer" cx="262" cy="219" r="120"/>
      <circle class="ring ring--inner" cx="262" cy="219" r="83"/>
      <text class="product-name" text-anchor="middle">
        <textPath href="#gel-top-arc" startOffset="50%">SHOWER GEL</textPath>
      </text>
      <text class="scent scent--bergamot" text-anchor="middle">
        <textPath href="#gel-bottom-arc" startOffset="50%">bergamot</textPath>
      </text>
      <circle class="brand-dot" cx="262" cy="192" r="7"/>
      <text class="brand-name" x="266" y="247" text-anchor="middle">KAELO</text>
      <text class="volume" x="264" y="420" text-anchor="middle">4 FL. OZ.</text>
    </svg>
  </section>

</main>
</body>
</html>
```